Mental Health

KVR HAVEN
Behavioral Health
4172 E. Dorrel St. Brenford, NV 89952
Marguerite (555)210-0142 / Ivan 555-210-0187

Email: KVRHaven@Qortamail.com
Newly Remodeled & Spacious
g Staff
Registered Nurses
Licensed Independent &
Professional Substance &
Abuse Counselors
Behavioral Health Techs
Certified Caregivers
Behavioral Health &
Substance Abuse Professionals

To Refer a Patient
About Us
KVR Haven is a Fully Staffed Behavioral
Health Residential Facility, providing
treatment plans for adults suffering
with various Behavioral Health and
Substance Abuse disorders, while living
in a nice safe, clean and supportive
environment. Our home offers clients the
ability to learn the necessary skills to
help clients adapt, build self confidence
as well as independence, with the goal
of reducing the probability of a future
crisis or possible relapse. We offer
counseling programs, consisting of a
variety of addiction and recovery support
groups, independent living, coping and
social skills groups, as well as assisting
clients with using tools to create a resume
to help obtain employment and so much
more. We are committed to teaching
self management care and allowing
clients to understand how to utilize the
resources, skills and tools available for
long term success by providing superior
quality, all-inclusive living arrangements
and treatment options.

Thank you for your patience while I update the final content needed for us to make the final decision this week.

```html
<!DOCTYPE html>
<html lang="en">
<head>
<meta charset="utf-8">
<title>KVR Haven – Business Card</title>
<link href="https://fonts.googleapis.com/css2?family=Marcellus&family=Poppins:wght@400;500&display=swap" rel="stylesheet">
<style>
  :root {
    --page-bg: #d9d4cc;
    --navy: #123f8f;
    --navy-deep: #0d3580;
    --blue-light: #2a63b5;
    --green: #5f9a3a;
    --green-dark: #3f8a2a;
    --frost-1: #eceae6;
    --frost-2: #d8d5cf;
    --text-light: #e9eef7;
    --brand-navy: #163b8c;
  }
  * { margin: 0; padding: 0; box-sizing: border-box; }
  html, body { width: 1200px; height: 970px; overflow: hidden; }
  body {
    background: var(--page-bg);
    display: flex;
    align-items: center;
    justify-content: center;
    font-family: "Poppins", sans-serif;
  }
  .business-card {
    position: relative;
    width: 1080px;
    height: 620px;
    border-radius: 22px;
    overflow: hidden;
    background: linear-gradient(160deg, var(--frost-1), var(--frost-2));
    box-shadow: 0 18px 40px rgba(0,0,0,0.18);
  }
  .card-shapes { position: absolute; inset: 0; }
  .contact-panel {
    position: absolute;
    left: 0; top: 0;
    width: 560px; height: 620px;
    color: var(--text-light);
  }
  .person-tab {
    position: absolute;
    left: -28px;
    width: 56px; height: 56px;
    border-radius: 50%;
    background: var(--green);
  }
  .person-name {
    position: absolute;
    left: 57px;
    font-family: "Marcellus", serif;
    font-size: 36px;
    letter-spacing: 1px;
    text-transform: uppercase;
    line-height: 1;
  }
  .contact-line {
    position: absolute;
    left: 59px;
    display: flex;
    align-items: flex-start;
    gap: 14px;
    font-size: 26px;
    line-height: 34px;
    font-weight: 400;
  }
  .contact-icon {
    flex: none;
    width: 31px; height: 31px;
    margin-top: 1px;
  }
  .brand {
    position: absolute;
    left: 595px;
    top: 273px;
    display: flex;
    align-items: center;
    gap: 22px;
  }
  .brand-dot {
    width: 64px; height: 64px;
    border-radius: 50%;
    background: var(--green-dark);
  }
  .brand-name {
    font-family: "Marcellus", serif;
    font-size: 56px;
    letter-spacing: 2px;
    color: var(--brand-navy);
    line-height: 1;
  }
</style>
</head>
<body>
  <div class="business-card">
    <svg class="card-shapes" width="1080" height="620" viewBox="0 0 1080 620" aria-hidden="true">
      <defs>
        <radialGradient id="panelGlow" cx="0.45" cy="0.35" r="0.7">
          <stop offset="0" stop-color="#2a63b5"/>
          <stop offset="1" stop-color="#0d3580"/>
        </radialGradient>
      </defs>
      <path d="M0 0 H553 Q415 310 553 620 H0 Z" fill="url(#panelGlow)"/>
      <path d="M553 0 Q415 310 553 620 L560 620 Q422 310 560 0 Z" fill="#3f8a2a"/>
    </svg>

    <div class="contact-panel">
      <span class="person-tab" style="top:89px"></span>
      <div class="person-name" style="top:100px">Marguerite</div>
      <div class="contact-line" style="top:151px">
        <svg class="contact-icon" viewBox="0 0 32 32" aria-hidden="true"><rect width="32" height="32" rx="5" fill="#5f9a3a"/><path d="M11 7c1 0 2 3 2.5 4.5.3.9-1.5 2-1.3 2.8.6 2 2.5 4 4.5 4.8.8.3 1.9-1.6 2.8-1.3 1.5.5 4.5 1.5 4.5 2.5 0 2-2 4.5-4 4.5C13 24.8 7 18.5 7 11c0-2 2-4 4-4z" fill="#e9eef7"/></svg>
        <span>(555)210-0142</span>
      </div>

      <span class="person-tab" style="top:247px"></span>
      <div class="person-name" style="top:260px">Ivan</div>
      <div class="contact-line" style="top:308px">
        <svg class="contact-icon" viewBox="0 0 32 32" aria-hidden="true"><rect width="32" height="32" rx="5" fill="#5f9a3a"/><path d="M11 7c1 0 2 3 2.5 4.5.3.9-1.5 2-1.3 2.8.6 2 2.5 4 4.5 4.8.8.3 1.9-1.6 2.8-1.3 1.5.5 4.5 1.5 4.5 2.5 0 2-2 4.5-4 4.5C13 24.8 7 18.5 7 11c0-2 2-4 4-4z" fill="#e9eef7"/></svg>
        <span>555-210-0187</span>
      </div>

      <div class="contact-line" style="top:395px">
        <svg class="contact-icon" viewBox="0 0 32 32" aria-hidden="true"><rect width="32" height="32" rx="5" fill="#5f9a3a"/><rect x="7" y="10" width="18" height="12" rx="1.5" fill="none" stroke="#e9eef7" stroke-width="2"/><path d="M7.5 11l8.5 6.5 8.5-6.5" fill="none" stroke="#e9eef7" stroke-width="2"/></svg>
        <span>KVRHaven@Qortamail.com</span>
      </div>

      <div class="contact-line" style="top:446px">
        <svg class="contact-icon" viewBox="0 0 32 32" aria-hidden="true"><rect width="32" height="32" rx="5" fill="#5f9a3a"/><path d="M16 6a7 7 0 0 0-7 7c0 5.5 7 13 7 13s7-7.5 7-13a7 7 0 0 0-7-7z" fill="#e9eef7"/><circle cx="16" cy="13" r="2.8" fill="#5f9a3a"/></svg>
        <span>4172 E. Dorrel St.<br>Brenford, NV 89952</span>
      </div>
    </div>

    <div class="brand">
      <span class="brand-dot"></span>
      <span class="brand-name">KVR HAVEN</span>
    </div>
  </div>
</body>
</html>
```